I need a new business card design for my pharmacy.

I need a business card design. I will include my logo.
The card needs to be readable. I prefer to have my logo on one side along with my website, the other side includes the other information. Please use combination of black, neon green, white, and silver. This needs to catch the eye but yet be clearly visible and legible. Thanks

Industry/Entity Type

Pharmacy

Contact Information for Business Card

It needs to have the following information listed:
Mel's Apothecary Owner/Pharm D.
7134 North Brook Lane
Sioux Falls, SD 57231
Phone 605-318-6207
Fax 605-318-6209
email: mel@melsapothecary-example.com
www.melsapothecary-example.com
Store hours Monday-Friday 8 am- 7 pm
Saturday 8 am- 12 pm
Sunday Closed
Please utilize the colors black, white, and neon green, maybe silver.

Requirements
Must have
• It needs to be easily readable!
Nice to have
• It should catch the eye.
Should not have
• Do not use any other colors except listed: black, neon green, white, & silver.

```html
<!DOCTYPE html>
<html lang="en">
<head>
<meta charset="utf-8">
<title>Mel's Apothecary Business Card</title>
<link rel="stylesheet" href="https://fonts.googleapis.com/css2?family=Open+Sans:wght@400;600;700;800&display=swap">
<style>
  :root {
    --black: #161616;
    --charcoal: #262626;
    --silver: #cfcfcf;
    --silver-light: #e6e6e6;
    --neon: #8cf03c;
    --white: #ffffff;
    --ink: #1e1e1e;
    --ink-soft: #4a4a4a;
    --page: #ececec;
  }
  * { box-sizing: border-box; margin: 0; padding: 0; }
  html, body { width: 1200px; height: 1000px; overflow: hidden; }
  body {
    background: var(--page);
    font-family: "Open Sans", Arial, sans-serif;
    position: relative;
  }
  .card {
    position: absolute;
    left: 250px;
    width: 700px;
    height: 400px;
    background: var(--black);
    overflow: hidden;
    box-shadow: 0 10px 30px rgba(0,0,0,.18);
  }
  .card--front { top: 60px; }
  .card--back { top: 540px; }

  .silver-band {
    position: absolute;
    left: 0; right: 0;
    background: linear-gradient(180deg, var(--silver-light), var(--silver));
  }

  /* Front */
  .card--front .silver-band { top: 135px; height: 165px; }
  .brand-lockup {
    position: absolute;
    display: flex; align-items: center; gap: 18px;
  }
  .brand-dot { border-radius: 50%; background: var(--neon); flex: none; }
  .card--front .brand-lockup { left: 150px; top: 30px; }
  .card--front .brand-dot { width: 34px; height: 34px; }
  .brand-name {
    font-weight: 700;
    color: var(--ink);
    letter-spacing: -0.5px;
  }
  .card--front .brand-name { font-size: 52px; line-height: 1; }
  .front-url {
    position: absolute; left: 202px; top: 100px;
    font-size: 26px; color: var(--ink-soft);
  }

  /* Back */
  .card--back .silver-band { top: 120px; height: 200px; }
  .back-brand { left: 26px; top: 22px; gap: 10px; }
  .back-brand .brand-dot { width: 16px; height: 16px; }
  .back-brand .brand-name { color: var(--white); font-size: 20px; }
  .holder-name {
    position: absolute; left: 230px; top: 62px;
    font-size: 40px; font-weight: 800; color: var(--neon);
    letter-spacing: 1px; line-height: 1;
  }
  .holder-title {
    position: absolute; left: 232px; top: 132px;
    font-size: 14px; font-weight: 700; color: var(--ink);
    letter-spacing: .5px;
  }
  .contact-list {
    position: absolute; left: 26px; top: 168px;
    list-style: none; display: flex; flex-direction: column; gap: 12px;
  }
  .contact-item { display: flex; align-items: center; gap: 10px; }
  .icon {
    width: 30px; height: 30px; border-radius: 50%;
    background: var(--white); border: 1px solid #b5b5b5;
    display: flex; align-items: center; justify-content: center; flex: none;
  }
  .contact-label { font-size: 10px; color: var(--ink); text-transform: uppercase; line-height: 1.2; }
  .contact-value { font-size: 12px; color: var(--ink-soft); line-height: 1.2; }
  .address {
    position: absolute; left: 232px; top: 160px;
    display: flex; align-items: center; gap: 8px;
    font-size: 12px; color: var(--ink); text-transform: uppercase;
  }
  .address .icon { width: 22px; height: 22px; }
  .hours {
    position: absolute; left: 232px; top: 202px;
    display: flex; gap: 10px;
  }
  .hours-title { font-size: 14px; color: var(--ink); text-transform: uppercase; margin-bottom: 4px; }
  .hours-table { border-collapse: collapse; font-size: 11px; color: var(--ink-soft); text-transform: uppercase; }
  .hours-table td { padding: 1px 18px 1px 0; }
  .back-url {
    position: absolute; right: 26px; bottom: 28px;
    font-size: 16px; color: var(--white);
  }
</style>
</head>
<body>

<section class="card card--front" aria-label="Business card, logo side">
  <div class="silver-band">
    <div class="brand-lockup">
      <span class="brand-dot"></span>
      <span class="brand-name">Mel's Apothecary</span>
    </div>
    <p class="front-url">www.melsapothecary-example.com</p>
  </div>
</section>

<section class="card card--back" aria-label="Business card, contact side">
  <div class="brand-lockup back-brand">
    <span class="brand-dot"></span>
    <span class="brand-name">Mel's Apothecary</span>
  </div>
  <h1 class="holder-name">REID T. CALLOWAY</h1>

  <div class="silver-band"></div>
  <p class="holder-title">MEL'S APOTHECARY OWNER/PHARM D.</p>

  <ul class="contact-list">
    <li class="contact-item">
      <span class="icon"><svg width="14" height="14" viewBox="0 0 24 24"><path d="M6.6 10.8a15 15 0 0 0 6.6 6.6l2.2-2.2a1 1 0 0 1 1-.25 11.4 11.4 0 0 0 3.6.57 1 1 0 0 1 1 1V20a1 1 0 0 1-1 1A17 17 0 0 1 3 4a1 1 0 0 1 1-1h3.5a1 1 0 0 1 1 1c0 1.25.2 2.45.57 3.57a1 1 0 0 1-.25 1z" fill="#555"/></svg></span>
      <div><p class="contact-label">Phone</p><p class="contact-value">605-318-6207</p></div>
    </li>
    <li class="contact-item">
      <span class="icon"><svg width="14" height="14" viewBox="0 0 24 24"><rect x="6" y="3" width="12" height="6" fill="#555"/><rect x="3" y="9" width="18" height="9" rx="2" fill="#555"/><rect x="7" y="14" width="10" height="7" fill="#fff" stroke="#555" stroke-width="1.5"/></svg></span>
      <div><p class="contact-label">Fax</p><p class="contact-value">605-318-6209</p></div>
    </li>
    <li class="contact-item">
      <span class="icon"><svg width="14" height="14" viewBox="0 0 24 24"><rect x="3" y="6" width="18" height="12" fill="none" stroke="#555" stroke-width="2"/><path d="M3 6l9 7 9-7" fill="none" stroke="#555" stroke-width="2"/></svg></span>
      <div><p class="contact-label">Email</p><p class="contact-value">mel@melsapothecary-example.com</p></div>
    </li>
  </ul>

  <p class="address">
    <span class="icon"><svg width="12" height="12" viewBox="0 0 24 24"><path d="M12 2a7 7 0 0 0-7 7c0 5 7 13 7 13s7-8 7-13a7 7 0 0 0-7-7zm0 9.5A2.5 2.5 0 1 1 12 6.5a2.5 2.5 0 0 1 0 5z" fill="#555"/></svg></span>
    7134 North Brook Lane, Sioux Falls, SD 57231
  </p>

  <div class="hours">
    <span class="icon"><svg width="16" height="16" viewBox="0 0 24 24"><circle cx="12" cy="12" r="9" fill="none" stroke="#555" stroke-width="2"/><path d="M12 7v5h4" fill="none" stroke="#555" stroke-width="2"/></svg></span>
    <div>
      <p class="hours-title">Store Hours</p>
      <table class="hours-table">
        <tr><td>Monday - Friday :</td><td>8:00 A.M. - 7:00 P.M.</td></tr>
        <tr><td>Saturday :</td><td>8:00 A.M. - 12:00 P.M.</td></tr>
        <tr><td>Sunday :</td><td>Closed</td></tr>
      </table>
    </div>
  </div>

  <p class="back-url">www.melsapothecary-example.com</p>
</section>

</body>
</html>
```